Business Card Design

I need a business card and logo for a new company based in Manhattan, Kansas called "Ferncliff Works, LLC". I am a project management consultant. I specialize in laying the foundation for businesses and business owners to get their projects on track. Think of it as if you were wanting to go from coast to coast on a train. Before you can jump on the train and sell tickets, you have to design the path the train will take, acquire the land, clear the trees, level the ground, prepare the base for the track, lay the track and finally place the train on the track (That's what I do with my clients). Once the train is on the track and I've provided them with the operations manual, then they and their managers get to drive the train. I don't have color preferences. The final design should communicate a clear direction or path to growing the customer's business.
Updates

Since I am in need of a logo as well, I have also created a logo design project that will work in conjunction with this project.

Reason: Accepted a company logo this afternoon that I would like to have cards designed around. Sorry for jumping the gun and posting both projects at the same time.

Industry/Entity Type

Business

Contact Information for Business Card

Owner: Dale Purvis. Business Name: Ferncliff Works, LLC. Business Address: 4871 Marlow Bend, Manhattan, KS, 66921. Business Phone Number: 785-640-1572. Business Email: dale@ferncliffworksllc.example

```html
<!DOCTYPE html>
<html lang="en">
<head>
<meta charset="utf-8">
<title>Ferncliff Works, LLC – Business Card</title>
<link rel="stylesheet" href="https://fonts.googleapis.com/css2?family=Noto+Sans:wght@400&display=swap">
<style>
  :root {
    --sky: #4cc8f5;
    --sky-line: #4ecbf6;
    --band-deep: #2b8fd6;
    --panel-top: #52cbf8;
    --panel-bottom: #43bff2;
    --paper: #ffffff;
    --ink-light: #ffffff;
  }
  * { margin: 0; padding: 0; box-sizing: border-box; }
  html, body {
    width: 1200px;
    height: 720px;
    overflow: hidden;
    background: var(--paper);
  }
  .card {
    position: relative;
    width: 1200px;
    height: 720px;
    background: var(--paper);
    font-family: "Noto Sans", "Segoe UI", sans-serif;
    overflow: hidden;
  }
  .top-rule {
    position: absolute;
    left: 0; top: 37px;
    width: 100%; height: 7px;
    background: var(--sky-line);
  }
  .company-name {
    position: absolute;
    left: 0; top: 112px;
    width: 100%;
    text-align: center;
    font-size: 84px;
    font-weight: 400;
    letter-spacing: 3px;
    line-height: 1.2;
    color: var(--sky);
  }
  .divider-band {
    position: absolute;
    left: 0; top: 337px;
    width: 100%; height: 8px;
    background: var(--band-deep);
  }
  .contact-panel {
    position: absolute;
    left: 0; top: 345px;
    width: 100%; height: 375px;
    background: linear-gradient(180deg, var(--panel-top), var(--panel-bottom));
  }
  .contact {
    position: absolute;
    left: 98px; top: 0;
    color: var(--ink-light);
  }
  .person-name {
    position: absolute;
    left: 98px; top: 378px;
    font-size: 68px;
    font-weight: 400;
    line-height: 1.1;
    letter-spacing: 1px;
    color: var(--ink-light);
    white-space: nowrap;
  }
  .label {
    position: absolute;
    left: 97px;
    font-size: 38px;
    line-height: 1;
    color: var(--ink-light);
    white-space: nowrap;
  }
  .value {
    position: absolute;
    left: 317px;
    font-size: 30px;
    line-height: 38px;
    letter-spacing: 0.5px;
    color: var(--ink-light);
    white-space: nowrap;
  }
  .label-address { top: 478px; }
  .value-address { top: 482px; }
  .label-phone { top: 574px; }
  .value-phone { top: 579px; }
  .label-email { top: 636px; }
  .value-email { top: 634px; }
</style>
</head>
<body>
  <div class="card">
    <div class="top-rule"></div>
    <h1 class="company-name">Ferncliff Works, LLC</h1>
    <div class="divider-band"></div>
    <div class="contact-panel" role="img" aria-label="Softly blurred photo of a smiling business team in suits, tinted sky blue"></div>
    <h2 class="person-name">Dale Purvis</h2>
    <span class="label label-address">Address :-</span>
    <p class="value value-address">4871 Marlow Bend, Manhattan, KS,<br>66921</p>
    <span class="label label-phone">Phone&nbsp;&nbsp; :-</span>
    <p class="value value-phone">785-640-1572.</p>
    <span class="label label-email">Email:-</span>
    <p class="value value-email">dale@ferncliffworksllc.example</p>
  </div>
</body>
</html>
```